One Pager Fact Sheet Design

I need a couple of headers and footer designed to use for information security fact sheets to give to customers. Similar to the one listed below.

```html
<!DOCTYPE html>
<html lang="en">
<head>
<meta charset="utf-8">
<title>Fact Sheet Headers and Footer</title>
<link href="https://fonts.googleapis.com/css2?family=Nunito:wght@800&family=Source+Sans+3:wght@400;600&display=swap" rel="stylesheet">
<style>
  :root {
    --red: #e41e26;
    --red-deep: #d9161d;
    --red-warm: #ee4a3a;
    --panel: #ebebeb;
    --strip: #f5f0f0;
    --white: #ffffff;
    --ink: #1a1a1a;
    --social: #1d8fd6;
  }
  html, body {
    margin: 0;
    padding: 0;
    width: 1200px;
    height: 766px;
    overflow: hidden;
    background: var(--white);
  }
  .canvas {
    position: relative;
    width: 1200px;
    height: 766px;
    overflow: hidden;
  }
  .top-strip {
    position: absolute;
    left: 40px; top: 0;
    width: 1127px; height: 17px;
    background: var(--strip);
  }
  .sheet-panel {
    position: absolute;
    left: 40px; top: 51px;
    width: 1127px; height: 665px;
    background: var(--panel);
  }
  .header {
    position: absolute;
    left: 73px;
    width: 1061px;
    overflow: hidden;
    background: linear-gradient(100deg, var(--red-warm) 0%, var(--red) 35%, var(--red-deep) 60%, var(--red) 100%);
  }
  .header--large { top: 97px; height: 228px; }
  .header--slim { top: 428px; height: 92px; }
  .header-texture {
    position: absolute;
    top: 0; bottom: 0;
    right: 0;
    background: radial-gradient(ellipse at 40% 50%, rgba(255,255,255,0.28) 0%, rgba(255,255,255,0.12) 35%, rgba(255,255,255,0) 70%),
                linear-gradient(90deg, rgba(255,255,255,0) 0%, rgba(255,255,255,0.1) 40%, rgba(255,255,255,0.16) 100%);
  }
  .header--large .header-texture { left: 500px; }
  .header--slim .header-texture { left: 560px; }
  .brand {
    position: absolute;
    display: flex;
    align-items: center;
    color: var(--white);
    font-family: "Nunito", sans-serif;
    font-weight: 800;
    letter-spacing: -0.5px;
    white-space: nowrap;
  }
  .brand-dot {
    border-radius: 50%;
    border: solid var(--white);
    box-sizing: border-box;
    flex: none;
  }
  .header--large .brand { left: 64px; top: 98px; font-size: 52px; gap: 18px; }
  .header--large .brand-dot { width: 52px; height: 52px; border-width: 7px; }
  .header--slim .brand { left: 42px; top: 24px; font-size: 34px; gap: 10px; }
  .header--slim .brand-dot { width: 40px; height: 40px; border-width: 5px; }
  .header-mark {
    position: absolute;
    right: 47px; top: 34px;
    width: 36px; height: 36px;
    border-radius: 50%;
    border: 5px solid var(--white);
    box-sizing: border-box;
  }
  .footer-rule {
    position: absolute;
    left: 73px; top: 580px;
    width: 1061px; height: 5px;
    background: var(--red);
  }
  .footer {
    position: absolute;
    left: 73px; top: 585px;
    width: 1061px; height: 88px;
    overflow: hidden;
    background: linear-gradient(100deg, #c9c9c9 0%, #e3e3e3 30%, #dedede 60%, #f0f0f0 100%);
  }
  .footer-texture {
    position: absolute;
    left: 560px; top: 0; bottom: 0; right: 0;
    background: radial-gradient(ellipse at 35% 40%, rgba(255,255,255,0.7) 0%, rgba(255,255,255,0.25) 40%, rgba(255,255,255,0) 75%);
  }
  .contact-row {
    position: absolute;
    left: 35px; right: 34px; top: 26px;
    display: flex;
    align-items: center;
    justify-content: space-between;
    font-family: "Source Sans 3", sans-serif;
    font-size: 15.5px;
    color: var(--ink);
    white-space: nowrap;
  }
  .contact-item { display: flex; align-items: center; gap: 6px; }
  .contact-icon {
    width: 21px; height: 21px;
    flex: none;
    border-radius: 50%;
    background: var(--red);
    display: flex; align-items: center; justify-content: center;
  }
  .contact-social { display: flex; align-items: center; }
  .contact-divider {
    width: 3px; height: 26px;
    background: var(--red);
    margin-right: 12px;
  }
  .social-list { display: flex; gap: 7px; margin-right: 8px; }
  .social-dot { width: 21px; height: 21px; border-radius: 50%; background: var(--social); }
</style>
</head>
<body>
<div class="canvas">
  <div class="top-strip"></div>
  <div class="sheet-panel"></div>

  <header class="header header--large">
    <div class="header-texture" role="img" aria-label="Faint circuit board lines around a security shield"></div>
    <div class="brand"><span class="brand-dot"></span>netwarden</div>
  </header>

  <header class="header header--slim">
    <div class="header-texture" role="img" aria-label="Faint circuit board lines around a security shield"></div>
    <div class="brand"><span class="brand-dot"></span>netwarden</div>
    <span class="header-mark"></span>
  </header>

  <div class="footer-rule"></div>
  <footer class="footer">
    <div class="footer-texture" role="img" aria-label="Faint circuit board lines around a security shield"></div>
    <div class="contact-row">
      <div class="contact-item">
        <span class="contact-icon">
          <svg width="13" height="13" viewBox="0 0 14 14" fill="none" stroke="#fff" stroke-width="1.4">
            <circle cx="7" cy="7" r="5.5"/><ellipse cx="7" cy="7" rx="2.4" ry="5.5"/><line x1="1.5" y1="7" x2="12.5" y2="7"/>
          </svg>
        </span>
        <span>netwarden.example&nbsp;&nbsp;netwarden.example.org</span>
      </div>
      <div class="contact-item">
        <span class="contact-icon">
          <svg width="12" height="12" viewBox="0 0 12 12"><path d="M1 1 L11 5 L6.5 6.5 L5 11 Z" fill="#fff"/></svg>
        </span>
        <span>social.example/company/netwarden</span>
      </div>
      <div class="contact-item">
        <span class="contact-icon">
          <svg width="13" height="11" viewBox="0 0 14 12" fill="#fff">
            <path d="M1 4 C1 1.5 13 1.5 13 4 L13 5 L10 5 L10 3.8 L4 3.8 L4 5 L1 5 Z"/>
            <rect x="3" y="6" width="8" height="5" rx="1"/>
          </svg>
        </span>
        <span>01632 960 482</span>
      </div>
      <div class="contact-social">
        <span class="contact-divider"></span>
        <div class="social-list">
          <span class="social-dot"></span><span class="social-dot"></span><span class="social-dot"></span><span class="social-dot"></span>
        </div>
        <span>@netwarden.example</span>
      </div>
    </div>
  </footer>
</div>
</body>
</html>
```